Website Design AI Digital Marketing Tool for Small Businesses

We are a marketing saas that is selling an app that allows business owners to launch digital marketing campaigns in one click. Our value proposition is to help them grow their business in one click with pre-vetted marketers armed with AI.

We want a modern website design that looks like a professional tech startup / saas. Use the same content on plovenda.io and make it look incredible. We want it to stand out and use big bold colors and text so that it's energetic and creative but still modern.

Pages are:
Home - plovenda.io
Pricing - plovenda.io/pricing
Features - https://plovenda.io/features/
Marketing - https://plovenda.io/marketing/

EXAMPLES
https://zantrel.example-sites.io/
https://moss-venture-sample-layout.example-sites.io/home-02

We really want a professional tech company feel. It needs to look like the best company with the best team in the world created it.

Target Market(s)

We are targeting small businesses to help them with their digital marketing

Industry/Entity Type

Tech

Coding

Coded - Design and coding required

Number of Pages Required

4 page

Font styles to use
Sans Serif
Other font styles liked:
• Work Sans

Colors
0094D4
00A9DD
6FCCEA
C7EBF8
E9F6FB

Requirements
Must have
• Modern, bright colors, same / similar content as existing site
Nice to have
• Big bold text and brand colors like quillrun - but also techy and modern
Should not have
• nothing that doesnt fit the brand

```html
<!DOCTYPE html>
<html lang="en">
<head>
<meta charset="utf-8">
<title>Plovenda — Automate Your Small Business Growth</title>
<link href="https://fonts.googleapis.com/css2?family=Montserrat:wght@400;500;600;700&family=Lato:wght@400;700&display=swap" rel="stylesheet">
<style>
:root{
  --bg:#eef0f5;
  --ink:#222428;
  --muted:#3d3f45;
  --cyan:#19d6e6;
  --cyan-soft:#9ee9f2;
  --purple:#ae3fe6;
  --purple-soft:#d9c4f1;
  --line:#3a3c40;
  --white:#ffffff;
}
*{box-sizing:border-box;margin:0;padding:0}
html,body{width:1200px;height:3851px;overflow:hidden;background:var(--bg)}
body{position:relative;font-family:'Lato',sans-serif;color:var(--ink)}
.abs{position:absolute}
.head{font-family:'Montserrat',sans-serif}
.blob{position:absolute;border-radius:50%;filter:blur(60px)}
.btn{position:absolute;display:flex;align-items:center;justify-content:center;font-family:'Montserrat',sans-serif;font-weight:700;font-size:15px;color:var(--white);letter-spacing:.2px}
.btn.cyan{background:var(--cyan)}
.btn.purple{background:var(--purple)}
.brand{display:flex;align-items:center;gap:10px;font-family:'Montserrat',sans-serif;font-weight:500;color:#2b2d31}
.brand .mark{width:34px;height:34px;border:4px solid var(--cyan)}
.nav-pill{left:443px;top:33px;width:314px;height:47px;border-radius:24px;background:#2a2c31;display:flex;align-items:center;padding-left:8px}
.nav-pill .home{width:50px;height:34px;border-radius:17px;background:var(--white);display:flex;align-items:center;justify-content:center}
.nav-pill a{color:#fff;font-family:'Montserrat',sans-serif;font-size:14px;text-decoration:none;margin-left:36px}
.nav-pill a+a{margin-left:30px}
.hero-title{left:0;width:1200px;top:235px;text-align:center;font-family:'Montserrat',sans-serif;font-weight:700;font-size:56px;line-height:77px}
.hero-sub{left:0;width:1200px;top:404px;text-align:center;font-size:15px}
.section-label{font-family:'Montserrat',sans-serif;font-size:15px;color:#333;display:flex;align-items:center}
.section-label .rule{width:48px;height:1px;background:#333;margin:0 24px 0 22px}
.h2{font-family:'Montserrat',sans-serif;font-weight:500;font-size:32px;line-height:43px}
.para{font-size:14.5px;line-height:26px;color:var(--muted)}
.partner{position:absolute;top:752px;width:202px;height:98px;background:var(--white);border-radius:6px;box-shadow:0 6px 18px rgba(40,40,70,.12);display:flex;align-items:center;justify-content:center;gap:8px;font-family:'Montserrat',sans-serif;font-weight:600;font-size:24px;color:#1f2024}
.partner .dot{width:14px;height:14px;background:#1f2024;border-radius:50%}
.accordion{left:641px;top:988px;width:447px}
.acc-row{height:68.5px;border-bottom:2px solid #55575c;display:flex;align-items:center;font-family:'Montserrat',sans-serif;font-size:21px}
.acc-row svg{margin-right:22px;flex:none}
.acc-row .plus{margin-left:auto;font-weight:700;font-size:20px}
.feature h4{font-family:'Montserrat',sans-serif;font-weight:600;font-size:15.5px;margin:8px 0 14px}
.feature p{font-size:11px;line-height:19px;color:#6c6e74}
.stat{position:absolute;top:2310px;width:120px;text-align:center}
.stat b{display:block;font-family:'Montserrat',sans-serif;font-weight:700;font-size:29px}
.stat span{font-size:13px;line-height:19px;color:#444}
.quote{left:210px;width:780px;top:2664px;text-align:center;font-size:22px;line-height:36px;color:#2f3136}
.marquee{left:-60px;top:3390px;white-space:nowrap;font-family:'Montserrat',sans-serif;font-size:80px;font-weight:500;color:#222;display:flex;align-items:center;gap:56px}
.marquee .dash{width:90px;height:6px;background:#222;display:inline-block}
.foot-col h5{font-family:'Montserrat',sans-serif;font-weight:600;font-size:18px;line-height:22px;margin-bottom:14px}
.foot-col a{display:block;font-size:14px;line-height:23px;color:#333;text-decoration:none}
</style>
</head>
<body>

<!-- soft background glows -->
<div class="blob" style="left:350px;top:120px;width:420px;height:420px;background:var(--purple-soft);opacity:.9"></div>
<div class="blob" style="left:560px;top:230px;width:300px;height:300px;background:var(--cyan-soft);opacity:.9"></div>
<div class="blob" style="left:240px;top:260px;width:260px;height:240px;background:var(--cyan-soft);opacity:.8"></div>
<div class="blob" style="left:-180px;top:1280px;width:300px;height:400px;background:var(--cyan-soft);opacity:.7"></div>
<div class="blob" style="left:1120px;top:2320px;width:260px;height:340px;background:var(--purple-soft);opacity:.8"></div>

<!-- header -->
<div class="abs brand" style="left:110px;top:30px;font-size:36px"><span class="mark"></span>plovenda</div>
<nav class="abs nav-pill">
  <span class="home"><svg width="18" height="16" viewBox="0 0 18 16"><path d="M9 1 1 8h2.5v7h4v-4.5h3V15h4V8H17z" fill="#222"/></svg></span>
  <a href="#">PLATFORM</a><a href="#">FEATURES</a>
</nav>
<a class="btn cyan" style="left:980px;top:35px;width:108px;height:45px">LOG IN</a>

<!-- hero -->
<h1 class="abs hero-title">The App to Automate Your<br>Small Business Growth</h1>
<p class="abs hero-sub">The Only Marketing Platform for Small Businesses that Handles Your Marketing in One Click.</p>
<a class="btn cyan" style="left:438px;top:470px;width:143px;height:43px">GET STARTED</a>
<a class="btn purple" style="left:602px;top:470px;width:160px;height:43px">HOW IT WORKS</a>

<!-- partners -->
<h2 class="abs head" style="left:0;width:1200px;top:668px;text-align:center;font-weight:600;font-size:29px">COMPANIES WE WORK WITH</h2>
<div class="partner" style="left:111px">Nimbrix</div>
<div class="partner" style="left:370px">Ledgerline</div>
<div class="partner" style="left:628px">Rankwell</div>
<div class="partner" style="left:887px"><span class="dot"></span>Peakmode</div>
<svg class="abs" style="left:576px;top:884px" width="48" height="10"><circle cx="5" cy="5" r="4" fill="#bde6f3"/><circle cx="24" cy="5" r="4.5" fill="var(--purple)"/><circle cx="43" cy="5" r="4" fill="#bde6f3"/></svg>

<!-- 01 services -->
<div class="abs section-label" style="left:111px;top:997px">01<span class="rule"></span>SERVICES</div>
<h2 class="abs h2" style="left:110px;top:1035px">Online Marketing Will<br>Never Be the Same</h2>
<p class="abs para" style="left:111px;top:1140px;width:430px">Get a Fortune-500 Quality Web Presence and a Personalized Action Plan</p>
<a class="btn cyan" style="left:111px;top:1217px;width:143px;height:44px">VIEW PRICING</a>
<a class="btn purple" style="left:276px;top:1217px;width:185px;height:44px">WHAT'S INCLUDED</a>

<div class="abs accordion">
  <div class="acc-row"><svg width="36" height="36" viewBox="0 0 36 36" fill="none" stroke="#222" stroke-width="1.8"><circle cx="18" cy="18" r="16"/><circle cx="18" cy="18" r="10"/><circle cx="18" cy="18" r="4"/><path d="M18 18 30 6"/></svg>Set Your Goals<span class="plus">+</span></div>
  <div class="acc-row"><svg width="36" height="36" viewBox="0 0 36 36" fill="none" stroke="#222" stroke-width="1.8"><rect x="5" y="5" width="22" height="28"/><path d="M11 13h10M11 19h10M11 25h6M28 10 20 28"/></svg>Get Detailed Action Plan<span class="plus">+</span></div>
  <div class="acc-row"><svg width="36" height="36" viewBox="0 0 36 36" fill="none" stroke="#222" stroke-width="1.8"><circle cx="8" cy="8" r="5"/><circle cx="28" cy="8" r="5"/><circle cx="8" cy="28" r="5"/><rect x="14" y="14" width="8" height="8"/><circle cx="28" cy="28" r="5"/></svg>Instant Marketing<span class="plus">+</span></div>
  <div class="acc-row"><svg width="36" height="36" viewBox="0 0 36 36" fill="none" stroke="#222" stroke-width="1.8"><rect x="3" y="5" width="30" height="22"/><path d="M3 11h30M12 33h12M18 27v6"/><circle cx="24" cy="19" r="4"/></svg>AI+ Web Creation<span class="plus">+</span></div>
  <div class="acc-row"><svg width="36" height="36" viewBox="0 0 36 36" fill="none" stroke="#222" stroke-width="1.8"><circle cx="18" cy="18" r="15"/><path d="M22 12h-6a3 3 0 0 0 0 6h4a3 3 0 0 1 0 6h-6M18 9v18"/></svg>Flexible Pricing<span class="plus">+</span></div>
  <div class="acc-row"><svg width="36" height="36" viewBox="0 0 36 36" fill="none" stroke="#222" stroke-width="1.8"><path d="M18 2c6 6 6 16 4 24h-8c-2-8-2-18 4-24z"/><path d="M14 20l-5 6 5 2M22 20l5 6-5 2M16 30l2 5 2-5"/><circle cx="18" cy="13" r="3"/></svg>Launch Campaign<span class="plus">+</span></div>
</div>

<!-- 02 best -->
<div class="abs section-label" style="left:111px;top:1519px">02<span class="rule"></span>BEST</div>
<h2 class="abs h2" style="left:110px;top:1558px">Plovenda the Best</h2>
<p class="abs para" style="left:111px;top:1625px;width:440px">The All in One Platform to Generate Personalized Suggestions and Hire Your Dream Team to Launch Winning Campaigns.</p>

<div class="abs feature" style="left:656px;top:1482px;width:430px">
  <svg width="40" height="38" viewBox="0 0 40 38" fill="none" stroke="var(--cyan)" stroke-width="1.8"><circle cx="24" cy="12" r="9"/><path d="M20 12l3 3 5-6M2 30l8-6h8l6 4h-8M2 36h16l14-8"/></svg>
  <h4>No More Broken Promises</h4>
  <p>We guarantee quality marketing professionals that deliver on time and communicate constantly.</p>
</div>
<div class="abs feature" style="left:656px;top:1615px;width:430px">
  <svg width="40" height="38" viewBox="0 0 40 38" fill="none" stroke="var(--cyan)" stroke-width="1.8"><rect x="16" y="2" width="18" height="20"/><path d="M25 6v12M2 30l8-6h8l6 4h-8M2 36h16l14-8"/></svg>
  <h4>Start at Nearly Any Budget</h4>
  <p>Simple, dynamic pricing within the budget you select. Only pay for what you use.</p>
</div>
<div class="abs feature" style="left:656px;top:1736px;width:430px">
  <svg width="32" height="32" viewBox="0 0 32 32" fill="none" stroke="var(--cyan)" stroke-width="1.8"><rect x="3" y="3" width="22" height="24"/><circle cx="16" cy="16" r="6"/><path d="M20 20l8 8"/></svg>
  <h4>Transparency &amp; Control</h4>
  <p>View campaign progress and update preferences at any time through our convenient application.</p>
</div>

<!-- 03 video -->
<div class="abs section-label" style="left:111px;top:1956px">03<span class="rule"></span>VIDEO</div>
<h2 class="abs h2" style="left:110px;top:1996px">Watch Plovenda AI Build an<br>SEO Optimized Website in<br>Minutes.</h2>
<p class="abs para" style="left:111px;top:2136px">Sign Up and Receive an Professional Designed Website Same Day*</p>
<a class="btn cyan" style="left:111px;top:2183px;width:143px;height:43px">VIEW PRICING</a>
<a class="btn purple" style="left:276px;top:2183px;width:159px;height:43px">HOW IT WORKS</a>

<div class="abs" role="img" aria-label="Video preview of a generated business website with a team meeting photo" style="left:624px;top:1960px;width:464px;height:320px;background:linear-gradient(180deg,#1b2452 0%,#1b2452 77%,#141b40 77%,#141b40 100%)">
  <div style="position:absolute;left:236px;top:0;width:192px;height:188px;background:linear-gradient(135deg,#6b6a6a,#3e3a38)"></div>
  <div style="position:absolute;left:190px;top:118px;width:78px;height:78px;border-radius:50%;background:var(--cyan);display:flex;align-items:center;justify-content:center"><svg width="26" height="28" viewBox="0 0 26 28"><path d="M3 2 24 14 3 26z" fill="#fff"/></svg></div>
</div>

<div class="stat" style="left:600px"><b>4K+</b><span>Websites Built</span></div>
<div class="stat" style="left:722px"><b>2K</b><span>Consulting Hours</span></div>
<div class="stat" style="left:855px"><b>2K</b><span>Avg Response<br>Time</span></div>
<div class="stat" style="left:983px"><b>99%</b><span>Avg Response<br>Time</span></div>

<!-- 04 testimonials -->
<div class="abs section-label" style="left:111px;top:2476px">04<span class="rule"></span>TESTIMONIALS</div>
<h2 class="abs h2" style="left:110px;top:2515px">What People Are Saying</h2>
<p class="abs para" style="left:111px;top:2575px">Just a Few Out of Thousands of Happy Customers.</p>
<svg class="abs" style="left:552px;top:2578px" width="96" height="70" viewBox="0 0 96 70"><path d="M2 0h40v34L26 70H8l12-28H2zM54 0h40v34L78 70H60l12-28H54z" fill="var(--purple-soft)"/></svg>
<svg class="abs" style="left:112px;top:2687px" width="14" height="20"><path d="M11 2 3 10l8 8" fill="none" stroke="#222" stroke-width="2"/></svg>
<svg class="abs" style="left:1075px;top:2687px" width="14" height="20"><path d="M3 2l8 8-8 8" fill="none" stroke="#222" stroke-width="2"/></svg>
<p class="abs quote">Plovenda did an excellent job recreating our website and is doing an excellent job servicing our account as well. I would highly recommend Plovenda for any business.</p>
<div class="abs" style="left:0;width:1200px;top:2795px;text-align:center;font-size:22px;font-weight:700;font-family:'Montserrat',sans-serif">Marcus T</div>
<div class="abs" style="left:0;width:1200px;top:2830px;text-align:center;font-size:20px;color:#555">Owner</div>

<!-- 05 digital marketing -->
<div class="abs section-label" style="left:111px;top:2996px">05<span class="rule"></span>DIGITAL MARKETING</div>
<h2 class="abs h2" style="left:110px;top:3035px">Let’s Make Something<br>Great Together</h2>
<p class="abs para" style="left:111px;top:3137px">Start With Your Free Digital Marketing Roadmap.</p>
<a class="btn cyan" style="left:111px;top:3194px;width:214px;height:44px">JOIN THE REVOLUTION</a>
<div class="abs" role="img" aria-label="Top-down photo of a team working with laptops, notes and coffee on a wooden table" style="left:636px;top:2935px;width:370px;height:370px;border-radius:50%;background:radial-gradient(circle at 45% 45%,#d9c3a4,#b69a7a 70%,#8e7558)"></div>

<!-- follow marquee -->
<div class="abs marquee"><span>s</span><span class="dash"></span><span>Follow Us</span><span class="dash"></span><span>Follow Us</span><span class="dash"></span></div>

<!-- footer -->
<footer>
  <div class="abs brand" style="left:118px;top:3585px;font-size:50px"><span class="mark" style="width:44px;height:44px;border-width:5px"></span>plovenda</div>
  <svg class="abs" style="left:113px;top:3665px" width="12" height="16" viewBox="0 0 12 16"><path d="M6 0a6 6 0 0 0-6 6c0 4 6 10 6 10s6-6 6-10a6 6 0 0 0-6-6zm0 8.5A2.5 2.5 0 1 1 6 3.5a2.5 2.5 0 0 1 0 5z" fill="#222"/></svg>
  <p class="abs" style="left:145px;top:3661px;font-size:14px;line-height:22px;color:#333">418 Orchard Row #12<br>Halden, OR 97021</p>
  <svg class="abs" style="left:112px;top:3727px" width="16" height="12" viewBox="0 0 16 12"><rect width="16" height="12" fill="#222"/><path d="M0 0l8 6 8-6" fill="none" stroke="#eef0f5" stroke-width="1.5"/></svg>
  <p class="abs" style="left:145px;top:3723px;font-size:14px;color:#333">ask@plovenda.io</p>

  <div class="abs foot-col" style="left:415px;top:3592px"><h5>Quick Links</h5><a href="#">Marketing</a><a href="#">Web Creation</a><a href="#">Automation</a></div>
  <div class="abs foot-col" style="left:580px;top:3592px"><h5>Account<br>Management</h5><a href="#">Login</a><a href="#">Account</a><a href="#">Support</a></div>
  <div class="abs foot-col" style="left:772px;top:3592px"><h5>Important Links</h5><a href="#">Privacy Policy</a><a href="#">Terms &amp; Conditions</a></div>
  <div class="abs foot-col" style="left:990px;top:3592px"><h5>Follow Us</h5><a href="#">Community</a><a href="#">Updates</a><a href="#">Videos</a></div>

  <div class="abs" style="left:110px;top:3775px;width:980px;height:1px;background:#c9cbd1"></div>
  <p class="abs" style="left:0;width:1200px;top:3804px;text-align:center;font-size:15px;color:#333">©Copyrights 2024 Plovenda &nbsp;| &nbsp; All Rights Reserved</p>
</footer>

</body>
</html>
```